IT Business Card Design

My company is a newly started small IT repair business. I operate outside of usual hours except for Saturday.
I am a very experienced and professional Technician.
I would like the business card to express that I am running a professional business and not some home IT business. This should be expressed through the design of the business card.
On the back of the card I would like the name of the company to be displayed.
Updates
Sorry guys, I have updated the requirement to be double sided. Fantastic submissions so far! Keep up the good work.
Hey designers!
Hey Designers!
Thank you all for your hard work!
Target Market(s)
Home to small business users.
Industry/Entity Type
Business
Contact Information for Business Card
Harbourline Computers
Marcus Pembrey (Director)
marcus.pembrey@quenmail.com.au
Operating Hours
5pm-12am Mon - Fri
9am - 5pm Sat
Mobile
0437915263
Requirements
Must have
- The base colour must be matte black. There must be some dark purple. (To go with the "Harbourline" theme)

```html
<!DOCTYPE html>
<html lang="en">
<head>
<meta charset="utf-8">
<title>Harbourline Computers – Business Card</title>
<link href="https://fonts.googleapis.com/css2?family=Advent+Pro:wght@200;300&family=Share+Tech+Mono&display=swap" rel="stylesheet">
<style>
  :root {
    --page: #e9e8ec;
    --navy: #2b3251;
    --navy-deep: #232a45;
    --pink: #d04a86;
    --plum: #7d3a6c;
    --stripe: #e6e6ea;
    --ink-light: #e8e8ee;
    --ink-soft: #c9cbd6;
    --shadow: rgba(20, 20, 30, 0.25);
  }
  * { margin: 0; padding: 0; box-sizing: border-box; }
  html, body {
    width: 1200px; height: 1200px; overflow: hidden;
    background: var(--page);
  }
  .sheet {
    width: 1200px; height: 1200px;
    display: flex; flex-direction: column; align-items: center; justify-content: center;
    gap: 56px;
  }
  .card {
    position: relative;
    width: 900px; height: 514px;
    box-shadow: 0 14px 30px var(--shadow);
  }
  .card-art { position: absolute; inset: 0; width: 100%; height: 100%; display: block; }
  .company-name {
    font-family: "Advent Pro", sans-serif;
    font-weight: 200;
    color: var(--ink-light);
    letter-spacing: 1px;
    line-height: 1;
    white-space: nowrap;
  }
  .card-front .company-name {
    position: absolute; left: 150px; top: 122px;
    font-size: 70px;
  }
  .contact {
    position: absolute; left: 200px; top: 232px;
    font-family: "Share Tech Mono", monospace;
    font-size: 19px;
    letter-spacing: 3px;
    color: var(--ink-soft);
    list-style: none;
    line-height: 30px;
  }
  .contact .hours-sat { margin-top: 18px; }
  .card-back .company-name {
    position: absolute; left: 0; right: 0; top: 210px;
    text-align: center;
    font-size: 84px;
  }
</style>
</head>
<body>
<main class="sheet">

  <section class="card card-front" aria-label="Business card front">
    <svg class="card-art" viewBox="0 0 900 514" aria-hidden="true">
      <defs>
        <linearGradient id="frameFront" x1="0" y1="0" x2="1" y2="0.4">
          <stop offset="0" stop-color="#d04a86"/>
          <stop offset="1" stop-color="#7d3a6c"/>
        </linearGradient>
        <radialGradient id="panelFront" cx="0.35" cy="0.3" r="0.9">
          <stop offset="0" stop-color="#2f3757"/>
          <stop offset="1" stop-color="#232a45"/>
        </radialGradient>
      </defs>
      <rect class="frame" width="900" height="514" fill="url(#frameFront)"/>
      <rect class="panel" x="42" y="42" width="816" height="430" fill="url(#panelFront)"/>
      <polygon class="corner-stripe" points="150,0 186,0 0,232 0,186" fill="var(--stripe)"/>
    </svg>
    <h1 class="company-name">Harbourline Computers</h1>
    <ul class="contact">
      <li>Marcus Pembrey (Director)</li>
      <li>marcus.pembrey@quenmail.com.au</li>
      <li>0437915263</li>
      <li>Operating Hours: Mon - Fri 5PM - 12AM</li>
      <li class="hours-sat">Sat 9AM - 5PM</li>
    </ul>
  </section>

  <section class="card card-back" aria-label="Business card back">
    <svg class="card-art" viewBox="0 0 900 514" aria-hidden="true">
      <defs>
        <linearGradient id="frameBack" x1="0" y1="0" x2="1" y2="0.4">
          <stop offset="0" stop-color="#d04a86"/>
          <stop offset="1" stop-color="#7d3a6c"/>
        </linearGradient>
        <radialGradient id="panelBack" cx="0.4" cy="0.3" r="0.9">
          <stop offset="0" stop-color="#2f3757"/>
          <stop offset="1" stop-color="#232a45"/>
        </radialGradient>
      </defs>
      <rect class="frame" width="900" height="514" fill="url(#frameBack)"/>
      <rect class="panel" x="42" y="42" width="816" height="430" fill="url(#panelBack)"/>
      <polygon class="corner-triangle" points="630,0 900,0 900,300" fill="var(--pink)" opacity="0.9"/>
      <polygon class="corner-stripe" points="0,300 0,344 150,514 190,514" fill="var(--stripe)"/>
    </svg>
    <h2 class="company-name">Harbourline Computers</h2>
  </section>

</main>
</body>
</html>
```